Ridgeway Spectral Studies Website

We are a paranormal research group located in Central Mississippi. We are a group dedicated to help the community in any paranormal investigation. We use fresh new techniques with cutting edge technology to investigate any paranormal situation. Our services are always free of charge to anyone. An unique feature of our group is that we provide a complete history of the property, courtesy of our research team. We would like to see designs that incorporate our logo. We are a professional group and want a professional website.. we will need a home page that will reflect out goals. Links will include "Home, About Us, Contact us, (MAYBE MORE). We will also want a "blank page" with same links that we can edit and fill in all the information..

Target Market(s)

Paranormal-Ghost hunting groups

Industry/Entity Type

Community

Coding

Coded - Design and coding required

Number of Pages Required

2 page

Font styles to use
Other font styles liked:

Requirements
Must have
• we will need a home page that will reflect out goals. Links will include "Home, About Us, Contact us, (MAYBE MORE). We will also want a "blank page" with same links that we can edit and fill in all the information..

```html
<!DOCTYPE html>
<html lang="en">
<head>
<meta charset="utf-8">
<title>Ridgeway Spectral Studies</title>
<link rel="stylesheet" href="https://fonts.googleapis.com/css2?family=Open+Sans:ital,wght@0,300;0,400;0,600;0,700;1,400&family=Oswald:wght@400;600&family=Marcellus+SC&display=swap">
<style>
:root{
  --ink:#0c0c0c;
  --white:#f2f2f2;
  --nav-text:#a8a8a8;
  --grey-text:#c9c9c9;
  --footer-text:#7a7a7a;
  --gold:#d9a514;
  --gold-dark:#6b5618;
  --gold-mid:#7c6420;
  --rust:#7a4310;
  --rust-text:#d68d33;
  --rule:#4a4630;
  --hero-top:#3a3a3a;
  --hero-mid:#222;
  --hero-low:#0f0f0f;
  --band-dark:#1b1b1b;
  --band-light:#4c4c4c;
}
*{margin:0;padding:0;box-sizing:border-box}
html,body{width:1168px;height:1200px;overflow:hidden;background:var(--ink)}
body{position:relative;font-family:"Open Sans",Arial,sans-serif;color:var(--white)}
.abs{position:absolute}

.hero-backdrop{left:0;top:0;width:1168px;height:773px;
  background:linear-gradient(180deg,var(--hero-top) 0%,var(--hero-mid) 45%,var(--hero-low) 100%);}

.topbar{left:0;top:0;width:1168px;height:63px;border-bottom:1px solid rgba(255,255,255,.18);background:rgba(0,0,0,.15)}
.nav{right:104px;top:23px;display:flex;gap:47px;list-style:none}
.nav li{font-size:15.5px;letter-spacing:2px;color:var(--nav-text)}
.nav li.active{color:var(--white)}

.brand{left:89px;top:180px;width:270px;display:flex;align-items:center;gap:12px}
.brand-dot{width:22px;height:22px;border-radius:50%;background:var(--white);flex:none}
.brand-name{font-size:24px;font-weight:400;color:var(--white);line-height:1.2}

.social{left:969px;top:186px;list-style:none}
.social li{display:flex;align-items:center;gap:8px;height:26px;margin-bottom:7px;font-size:13.5px}
.social .dot{width:26px;height:26px;border-radius:50%;background:#0a0a0a;border:1px solid #555}

.tagline{left:400px;top:329px;width:665px;text-align:right;font-family:"Marcellus SC",serif;font-size:21px;letter-spacing:1px;color:var(--white)}

.band-rule{left:0;width:1168px;height:1px;background:var(--rule)}

.intro-title{left:104px;top:445px;font-size:33px;font-weight:400;line-height:38px;letter-spacing:1px;text-transform:uppercase}
.intro-copy{left:104px;top:565px;width:404px;font-size:13.6px;line-height:17px;color:var(--grey-text)}
.know-more{left:105px;top:674px;width:131px;height:36px;background:linear-gradient(180deg,var(--gold-mid),var(--gold-dark));
  font-family:Oswald,sans-serif;font-size:19px;color:var(--white);display:flex;align-items:center;justify-content:center}

.agent-photo{left:544px;top:483px;width:213px;height:212px;
  background:linear-gradient(160deg,#3a3a3a 0%,#1e1e1e 60%,#0d0d0d 100%)}
.questions{left:773px;top:483px;width:272px;height:212px;background:var(--gold);padding:15px 16px 0 16px;color:#2a1e00}
.questions h2{font-family:Oswald,sans-serif;font-weight:600;font-size:21px;color:var(--white);letter-spacing:.5px;margin-bottom:18px}
.questions p{font-size:12.6px;line-height:16px}
.questions b{font-weight:700;color:#1a1200}
.questions .hours{color:var(--white);margin-top:14px}
.questions em{display:block;color:var(--white)}
.more-tab{left:1045px;top:483px;width:46px;height:212px;background:var(--rust);overflow:hidden}
.more-tab span{position:absolute;left:50%;top:50%;transform:translate(-50%,-50%) rotate(-90deg);white-space:nowrap;
  font-family:Oswald,sans-serif;font-size:25px;color:var(--rust-text)}

.features{left:0;top:773px;width:1168px;height:338px;
  background:linear-gradient(90deg,var(--band-dark) 0%,var(--band-dark) 30%,var(--band-light) 55%,#2e2e2e 80%,var(--band-dark) 100%);}
.feature{top:791px;width:290px;text-align:center}
.feature svg{display:block;margin:0 auto}
.feature h3{font-family:Oswald,sans-serif;font-weight:600;font-size:22px;letter-spacing:1.5px;margin-top:6px;text-transform:uppercase}
.feature p{font-size:14.6px;line-height:18px;margin:12px auto 0;width:272px}

.footer{left:0;top:1111px;width:1168px;height:89px;background:linear-gradient(90deg,#0e0e0e 0%,#151515 40%,#222 70%,#111 100%);border-top:1px solid #2a2a2a}
.footer p{position:absolute;left:83px;font-size:14.6px;color:var(--footer-text)}
</style>
</head>
<body>
<div class="abs hero-backdrop" role="img" aria-label="Dark misty forest at night with bare trees, moonlit sky and a raven on a branch"></div>

<header class="abs topbar">
  <ul class="abs nav">
    <li class="active">HOME</li>
    <li>ABOUT US</li>
    <li>CONTACT US</li>
  </ul>
</header>

<div class="abs brand"><span class="brand-dot"></span><span class="brand-name">Ridgeway Spectral Studies</span></div>

<ul class="abs social">
  <li><span class="dot"></span>socialpage</li>
  <li><span class="dot"></span></li>
  <li><span class="dot"></span></li>
</ul>

<p class="abs tagline">Ridgeway Center for Spectral Investigation &amp; Research</p>

<div class="abs band-rule" style="top:404px"></div>

<h1 class="abs intro-title">Ridgeway<br>Spectral<br>Studies</h1>
<p class="abs intro-copy">Praesent vestibulum aenean nonummy hendrerit mauris. Cum sociis natoque penatibus et magnis dis parturient montes ascetur ridiculus mus. Nulla dui. Fusce feugiat malesuada odio. Morbi nunc odio gravida at cursus nec luctus a lorem. Maece-nas tristique orci ac sem. Duis ultricies pharetra magna.</p>
<div class="abs know-more">know more...</div>

<div class="abs agent-photo" role="img" aria-label="Investigator in a dark suit holding a flashlight"></div>
<section class="abs questions">
  <h2>QUESTIONS?</h2>
  <p><b>Call:</b> 01555-010-42-17<br><b>Email:</b> info@ridgewayspectral.org</p>
  <p class="hours">Agents available for assistance -<em>7AM-9PM PT</em><em>After hour inquiries will be addressed within 24 hours.</em></p>
</section>
<div class="abs more-tab"><span>More Information...</span></div>

<div class="abs band-rule" style="top:740px"></div>

<section class="abs features" role="img" aria-label="Abstract grey geometric background"></section>

<article class="abs feature" style="left:105px">
  <svg width="100" height="106" viewBox="0 0 104 108" aria-hidden="true">
    <g fill="none" stroke="#fff" stroke-width="4">
      <ellipse cx="52" cy="54" rx="18" ry="50"/>
      <ellipse cx="52" cy="54" rx="18" ry="50" transform="rotate(60 52 54)"/>
      <ellipse cx="52" cy="54" rx="18" ry="50" transform="rotate(-60 52 54)"/>
    </g>
    <text x="52" y="62" text-anchor="middle" font-family="Oswald,sans-serif" font-size="22" font-weight="600" fill="#fff">1</text>
  </svg>
  <h3>Investigations</h3>
  <p>A visit from a family members causes unrest but more is at hand then just a visit from Grandpa. The team works to put all the pieces together to ex-plain all the activity.</p>
</article>

<article class="abs feature" style="left:441px">
  <svg width="100" height="106" viewBox="0 0 104 108" aria-hidden="true">
    <g fill="none" stroke="#fff" stroke-width="4">
      <ellipse cx="52" cy="54" rx="18" ry="50"/>
      <ellipse cx="52" cy="54" rx="18" ry="50" transform="rotate(60 52 54)"/>
      <ellipse cx="52" cy="54" rx="18" ry="50" transform="rotate(-60 52 54)"/>
    </g>
    <text x="52" y="62" text-anchor="middle" font-family="Oswald,sans-serif" font-size="22" font-weight="600" fill="#fff">2</text>
  </svg>
  <h3>Ghost Hunting</h3>
  <p>What is ghost hunting?<br>some of the do's and don'ts. Find out more about what we do and our opin-ion on Ghost hunting. What does it take to find the proof to satisfy the skeptics?</p>
</article>

<article class="abs feature" style="left:771px">
  <svg width="100" height="106" viewBox="0 0 104 108" aria-hidden="true">
    <g fill="none" stroke="#fff" stroke-width="4">
      <ellipse cx="52" cy="54" rx="18" ry="50"/>
      <ellipse cx="52" cy="54" rx="18" ry="50" transform="rotate(60 52 54)"/>
      <ellipse cx="52" cy="54" rx="18" ry="50" transform="rotate(-60 52 54)"/>
    </g>
    <text x="52" y="62" text-anchor="middle" font-family="Oswald,sans-serif" font-size="22" font-weight="600" fill="#fff">3</text>
  </svg>
  <h3>News</h3>
  <p>Praesent vestibulum aenean non-ummy hendrerit mauris. Cum sociis natoque penatibus et magnis dis par-turient montes ascetur ridiculus mus. Nulla dui.</p>
</article>

<footer class="abs footer">
  <p style="top:16px">RIDGEWAY SPECTRAL STUDIES</p>
  <p style="top:38px">Copyright © 2014 &nbsp;| All Rights Reserved</p>
</footer>
</body>
</html>
```